furniture and home contents restoration

I need to list the services that we perform in our studio.
we serve the general public as well as the insurance/ remediation industry

```html
<!DOCTYPE html>
<html lang="en">
<head>
<meta charset="utf-8">
<title>Keystone Refinishers – Business Card</title>
<link rel="stylesheet" href="https://fonts.googleapis.com/css2?family=PT+Serif:wght@400&display=swap">
<style>
  :root {
    --page: #ffffff;
    --card-navy: #23323d;
    --gold: #d39b3c;
    --ivory: #f4f1ea;
    --serif: "PT Serif", Georgia, serif;
  }
  * { box-sizing: border-box; margin: 0; padding: 0; }
  html, body { width: 1200px; height: 900px; overflow: hidden; background: var(--page); }
  body { position: relative; font-family: var(--serif); color: var(--ivory); }

  .card {
    position: absolute;
    left: 287px;
    width: 633px;
    height: 362px;
    background: var(--card-navy);
    overflow: hidden;
  }
  .card--back { top: 76px; }
  .card--front { top: 467px; }

  /* Services side */
  .services-title {
    position: absolute; top: 32px; left: 0; width: 100%;
    text-align: center; font-size: 15px; letter-spacing: 4px;
    color: var(--gold); line-height: 18px;
  }
  .service-list {
    position: absolute; top: 63px; list-style: none;
  }
  .service-list--left { left: 18px; }
  .service-list--right { left: 321px; }
  .service-list li {
    position: relative; padding-left: 17px;
    font-size: 13px; line-height: 21px; white-space: nowrap;
    text-transform: uppercase;
  }
  .service-list li svg {
    position: absolute; left: 0; top: 5px; width: 11px; height: 11px;
  }
  .assessment-band {
    position: absolute; left: 0; top: 302px; width: 100%; height: 60px;
    background: var(--gold);
    display: flex; flex-direction: column; justify-content: center; align-items: center;
    font-size: 12.5px; line-height: 16px; text-transform: uppercase; color: var(--ivory);
  }

  /* Contact side */
  .company-name {
    position: absolute; left: 54px; top: 42px;
    font-size: 49px; line-height: 54px; color: var(--ivory); font-weight: 400;
  }
  .company-field {
    position: absolute; left: 306px; top: 69px;
    font-size: 17.5px; line-height: 22px; white-space: nowrap;
  }
  .tagline {
    position: absolute; left: 306px; top: 109px; width: 272px;
    text-align: center; font-size: 12.5px; line-height: 16px;
    color: var(--gold); text-transform: uppercase;
  }
  .contact-person {
    position: absolute; left: 54px; top: 192px;
    font-size: 20px; line-height: 24px; color: var(--gold); letter-spacing: 0.3px;
  }
  .phone-list { position: absolute; left: 55px; top: 231px; list-style: none; }
  .phone-list li {
    display: flex; align-items: center; height: 26px;
    font-size: 17px;
  }
  .phone-list svg, .email svg { width: 16px; height: 16px; margin-right: 12px; flex: none; }
  .address {
    position: absolute; left: 351px; top: 231px;
    font-size: 17px; line-height: 21px; font-style: normal; text-transform: uppercase;
  }
  .email {
    position: absolute; left: 354px; top: 281px;
    display: flex; align-items: center; font-size: 17px; height: 26px;
  }
  .front-band {
    position: absolute; left: 0; bottom: 0; width: 100%; height: 12px;
    background: var(--gold);
  }
</style>
</head>
<body>

<section class="card card--back" aria-label="Services">
  <h2 class="services-title">SERVICES</h2>
  <ul class="service-list service-list--left">
    <li><svg viewBox="0 0 10 10"><path d="M5 0 10 5 5 10 0 5Z" fill="#d39b3c"/></svg>Antique repair and restoration</li>
    <li><svg viewBox="0 0 10 10"><path d="M5 0 10 5 5 10 0 5Z" fill="#d39b3c"/></svg>Art cleaning and remounting</li>
    <li><svg viewBox="0 0 10 10"><path d="M5 0 10 5 5 10 0 5Z" fill="#d39b3c"/></svg>Art and mirror frame repair</li>
    <li><svg viewBox="0 0 10 10"><path d="M5 0 10 5 5 10 0 5Z" fill="#d39b3c"/></svg>Chandelier cleaning and restoration</li>
    <li><svg viewBox="0 0 10 10"><path d="M5 0 10 5 5 10 0 5Z" fill="#d39b3c"/></svg>Document restoration</li>
    <li><svg viewBox="0 0 10 10"><path d="M5 0 10 5 5 10 0 5Z" fill="#d39b3c"/></svg>Glass, ceramic, and mirror repair</li>
    <li><svg viewBox="0 0 10 10"><path d="M5 0 10 5 5 10 0 5Z" fill="#d39b3c"/></svg>Hardware repair and restoration</li>
    <li><svg viewBox="0 0 10 10"><path d="M5 0 10 5 5 10 0 5Z" fill="#d39b3c"/></svg>Kitchen removal and reinstallation</li>
    <li><svg viewBox="0 0 10 10"><path d="M5 0 10 5 5 10 0 5Z" fill="#d39b3c"/></svg>Lamp cleaning and restoration</li>
    <li><svg viewBox="0 0 10 10"><path d="M5 0 10 5 5 10 0 5Z" fill="#d39b3c"/></svg>Lamp shade replacement</li>
  </ul>
  <ul class="service-list service-list--right">
    <li><svg viewBox="0 0 10 10"><path d="M5 0 10 5 5 10 0 5Z" fill="#d39b3c"/></svg>Metal polishing and restoration</li>
    <li><svg viewBox="0 0 10 10"><path d="M5 0 10 5 5 10 0 5Z" fill="#d39b3c"/></svg>Odor removal and ozone services</li>
    <li><svg viewBox="0 0 10 10"><path d="M5 0 10 5 5 10 0 5Z" fill="#d39b3c"/></svg>Photo restoration</li>
    <li><svg viewBox="0 0 10 10"><path d="M5 0 10 5 5 10 0 5Z" fill="#d39b3c"/></svg>Upholstery cleaning and deodorizing</li>
    <li><svg viewBox="0 0 10 10"><path d="M5 0 10 5 5 10 0 5Z" fill="#d39b3c"/></svg>In-house upholstery and reupholstery</li>
    <li><svg viewBox="0 0 10 10"><path d="M5 0 10 5 5 10 0 5Z" fill="#d39b3c"/></svg>Rug cleaning and restoration</li>
    <li><svg viewBox="0 0 10 10"><path d="M5 0 10 5 5 10 0 5Z" fill="#d39b3c"/></svg>Musical instrument restoration</li>
    <li><svg viewBox="0 0 10 10"><path d="M5 0 10 5 5 10 0 5Z" fill="#d39b3c"/></svg>Window treatment repair/ restoration</li>
    <li><svg viewBox="0 0 10 10"><path d="M5 0 10 5 5 10 0 5Z" fill="#d39b3c"/></svg>Leather restoration and replacement</li>
    <li><svg viewBox="0 0 10 10"><path d="M5 0 10 5 5 10 0 5Z" fill="#d39b3c"/></svg>Piano restoration and repair</li>
  </ul>
  <div class="assessment-band">
    <p>On-site inspections and desk review services</p>
    <p>Assessment reports and estimates for repair and restoration</p>
  </div>
</section>

<section class="card card--front" aria-label="Contact">
  <h1 class="company-name">Keystone<br>Refinishers</h1>
  <p class="company-field">HOME CONTENTS RESTORATION</p>
  <p class="tagline">Serving the general public and the insurance industry for over 40 years</p>

  <p class="contact-person">DANIEL FERRANTE</p>
  <ul class="phone-list">
    <li><svg viewBox="0 0 16 16" aria-label="Office phone"><path d="M3.5 1.5 6 4 4.7 6.2c.9 2 2.4 3.5 4.4 4.4L11 9.3l2.5 2.5-1.6 2.2C7 14 2 9 2 3.1Z" fill="none" stroke="#d39b3c" stroke-width="1.5" stroke-linejoin="round"/><path d="M9 2.5a4.5 4.5 0 0 1 4.5 4.5M9 5a2 2 0 0 1 2 2" fill="none" stroke="#d39b3c" stroke-width="1.3"/></svg>555.210.4800</li>
    <li><svg viewBox="0 0 16 16" aria-label="Mobile phone"><rect x="4" y="1" width="8" height="14" rx="1.5" fill="none" stroke="#d39b3c" stroke-width="1.6"/><rect x="6" y="12" width="4" height="1.2" fill="#d39b3c"/></svg>555.386.1947</li>
    <li><svg viewBox="0 0 16 16" aria-label="Fax"><rect x="1" y="5" width="3" height="10" rx="1" fill="#d39b3c"/><rect x="5" y="5" width="10" height="10" rx="1" fill="#d39b3c"/><rect x="7" y="1" width="6" height="4" fill="none" stroke="#d39b3c" stroke-width="1.2"/><g fill="#23323d"><rect x="7" y="7" width="6" height="2"/><rect x="7" y="10.5" width="1.5" height="1.5"/><rect x="9.3" y="10.5" width="1.5" height="1.5"/><rect x="11.5" y="10.5" width="1.5" height="1.5"/></g></svg>555.210.4815</li>
  </ul>

  <address class="address">118 Orchard Hill Rd.<br>Millbrook, NY 10599</address>
  <p class="email"><svg viewBox="0 0 16 16" aria-label="Email"><rect x="1.5" y="3.5" width="13" height="9" fill="none" stroke="#d39b3c" stroke-width="1.5"/><path d="M1.5 3.5 8 9l6.5-5.5M1.5 12.5 6 8m8.5 4.5L10 8" fill="none" stroke="#d39b3c" stroke-width="1.3"/></svg>SHOP@KEYSTONERF.COM</p>

  <div class="front-band"></div>
</section>

</body>
</html>
```